Lumo Grill-Wrap Stationery Design Project

We are a factory of the Doner kebab to distribute for restaurants and supermarkets.

what I need is

1- Presentation Folders cover for (Brochure , Letter and Business Card), the size ( 9"x12" Closed)

2- Envelopes, Size (DL , C5 and C4)

3- Letterhead (Standard).

Target Market(s)

Restaurants and supermarkets

Industry/Entity Type

Business

Requirements
Must have
• -Try to make the design related to the Business.

-Choose the same colors of the logo (Yellow, red and white).

-Try to make it seriously and high class business.

- The main logo with white background

```html
<!DOCTYPE html>
<html lang="en">
<head>
<meta charset="utf-8">
<title>Lumo Grill-Wrap Letterhead</title>
<link href="https://fonts.googleapis.com/css2?family=Lato:wght@400;700&display=swap" rel="stylesheet">
<style>
  :root {
    --backdrop: #e3e3e3;
    --paper: #ffffff;
    --brand-red: #a81c24;
    --brand-gold: #c9a227;
    --ink: #5a5a5a;
    --ghost: #ebebeb;
  }
  html, body {
    margin: 0;
    padding: 0;
    width: 1200px;
    height: 1000px;
    overflow: hidden;
    background: var(--backdrop);
    font-family: "Lato", sans-serif;
  }
  .letterhead {
    position: absolute;
    left: 282px;
    top: 50px;
    width: 636px;
    height: 900px;
    background: var(--paper);
    box-shadow: 0 2px 6px rgba(0,0,0,0.12);
    overflow: hidden;
  }
  .brand {
    position: absolute;
    left: 44px;
    top: 150px;
    display: flex;
    align-items: center;
    gap: 8px;
  }
  .brand-dot {
    width: 14px;
    height: 14px;
    border-radius: 50%;
    background: var(--brand-gold);
  }
  .brand-name {
    font-size: 20px;
    font-weight: 400;
    color: var(--brand-red);
    letter-spacing: 0.5px;
    margin: 0;
  }
  .contact {
    position: absolute;
    right: 40px;
    top: 56px;
    list-style: none;
    margin: 0;
    padding: 0;
    font-size: 8px;
    line-height: 11px;
    color: var(--ink);
  }
  .contact li {
    display: flex;
    align-items: center;
    gap: 5px;
  }
  .contact svg {
    width: 7px;
    height: 7px;
    fill: var(--brand-red);
    flex: none;
  }
  .watermark {
    position: absolute;
    left: 0;
    right: 0;
    top: 300px;
    margin: 0;
    text-align: center;
    font-size: 84px;
    font-weight: 400;
    line-height: 1.05;
    color: var(--ghost);
    letter-spacing: 1px;
  }
</style>
</head>
<body>
  <main class="letterhead">
    <div class="brand">
      <span class="brand-dot"></span>
      <h1 class="brand-name">Lumo Grill-Wrap</h1>
    </div>

    <ul class="contact">
      <li><svg viewBox="0 0 10 10"><path d="M5 0a3.5 3.5 0 0 0-3.5 3.5C1.5 6 5 10 5 10s3.5-4 3.5-6.5A3.5 3.5 0 0 0 5 0zm0 5a1.5 1.5 0 1 1 0-3 1.5 1.5 0 0 1 0 3z"/></svg>12 Mill Road, Eastvale, Postal Code</li>
      <li><svg viewBox="0 0 10 10"><path d="M2 0h2l1 2.5-1.3 1a6 6 0 0 0 2.8 2.8l1-1.3L10 6v2a2 2 0 0 1-2 2A8 8 0 0 1 0 2a2 2 0 0 1 2-2z"/></svg>555-010-4-22</li>
      <li><svg viewBox="0 0 10 10"><path d="M0 2h10v6H0zM0 2l5 3.5L10 2"/></svg>info@lumogrillwrap.com</li>
      <li><svg viewBox="0 0 10 10"><rect x="0" y="1" width="10" height="8" rx="1"/></svg>www.lumogrillwrap.com</li>
    </ul>

    <p class="watermark" aria-hidden="true">Lumo<br>Grill-Wrap</p>
  </main>
</body>
</html>
```